Plumbing Website

Design a simple 4 page website based on our provided logo and sketches. Winning designer should be willing to upgrade as needed (for additional fee). A design that includes SEO features is a plus.
I would like to see Home, , Services, Recent Jobs (set up for pictures), Contact. I like the water dropplet back ground. Please dont put logo in a box. File attached as exaple only, I am looking for a request service now button in the middle that will have a form fill to be emailed to two different addresses,
I would like to see vibrant colors. Examples of sites I like are www.brightvalvepipeworks.com look also at www.kmt-keystonemeridianpipes.com - this site is too busy but has good seo features.
Industry/Entity Type
Plumbing
Look and feel

```html
<!DOCTYPE html>
<html lang="en">
<head>
<meta charset="utf-8">
<title>Sierra Crest Plumbing</title>
<link href="https://fonts.googleapis.com/css2?family=Montserrat:wght@700;800&family=Open+Sans:wght@400;700&family=Roboto+Condensed:wght@400&family=Lora:wght@400&family=Arimo:wght@400;700&display=swap" rel="stylesheet">
<style>
:root{
  --red:#e8202a;
  --blue:#1f6fc0;
  --navy:#1a5aa8;
  --panel:#e3e3e3;
  --text:#222;
  --footer:#121212;
  --footer-bar:#2a2a2a;
  --link-blue:#4aa8e8;
}
*{box-sizing:border-box;margin:0;padding:0}
html,body{width:1159px;height:1200px;overflow:hidden}
body{font-family:"Open Sans",Arial,sans-serif;color:var(--text);background:#fff;position:relative}
.abs{position:absolute}

/* header */
.site-header{left:0;top:0;width:1159px;height:103px;background:linear-gradient(#dcecf8,#fff 70%)}
.brand{left:236px;top:26px;display:flex;align-items:center;gap:10px}
.brand-name{font-family:"Open Sans",sans-serif;font-weight:700;font-size:24px;color:var(--blue);line-height:1.05;width:140px}
.brand-mark{width:16px;height:16px;border-radius:50%;background:var(--blue)}
.call{left:690px;top:64px;font-family:"Roboto Condensed",sans-serif;font-size:21px;color:var(--navy);white-space:nowrap}
.call .num{font-family:"Lora",serif;font-size:26px;color:#111;margin-left:6px}

/* nav */
.main-nav{left:0;top:103px;width:1159px;height:31px;background:var(--red)}
.main-nav a{position:absolute;top:8px;color:#fff;text-decoration:none;font-family:"Roboto Condensed",sans-serif;font-size:13px}

/* hero */
.hero-band{left:0;top:134px;width:1159px;height:229px;background:linear-gradient(180deg,#2a76c4,#1f68b6)}
.hero{left:209px;top:134px;width:741px;height:229px;border:1px solid #555;overflow:hidden}
.hero-photo{width:100%;height:100%;background:linear-gradient(90deg,#efece6 0%,#e2d8c4 35%,#f2f2f2 60%,#cfd6dc 100%)}
.hero-text{left:33px;top:10px;font-family:"Montserrat",sans-serif;font-weight:800;color:var(--red);font-size:17px;line-height:25px;letter-spacing:.2px;white-space:nowrap}
.hero-arrow{top:88px}
.hero-dots{left:340px;top:207px;display:flex;gap:3px;background:var(--red);padding:3px 6px}
.hero-dots span{width:10px;height:10px;background:#fff;font-size:7px;text-align:center;line-height:10px;color:#333}
.hero-dots span+span{background:#bbb}

/* content */
.drops{top:363px;height:604px;background:radial-gradient(circle at 30% 40%,#e6f1fb,#a9cdee 80%)}
.drops.left{left:0;width:209px}
.drops.right{left:950px;width:209px}
.content{left:209px;top:363px;width:741px;height:604px;background:linear-gradient(#a7cfee,#fff 40px)}
.welcome{left:226px;top:385px;width:485px}
.welcome h1{font-family:"Arimo",Arial,sans-serif;font-weight:400;font-size:19.5px;color:#111;margin-bottom:8px}
.welcome p{font-size:9px;line-height:13px;margin-bottom:13px}
.service{left:226px;width:485px}
.service h2{height:29px;background:var(--red);color:#fff;font-family:"Montserrat",sans-serif;font-weight:700;font-size:13px;letter-spacing:.8px;padding:7px 0 0 20px}
.service .body{background:var(--panel);padding:6px 15px 6px 11px;font-size:9px;line-height:13px;text-align:justify}
.service .thumb{float:left;width:97px;height:68px;margin:0 8px 4px 0;border:1px solid #777;background:linear-gradient(135deg,#f4f4f4,#c9c9c9 60%,#e44 92%)}

.side-box{left:729px;width:200px;background:linear-gradient(#f2f2f2,#dcdcdc);border-radius:3px}
.side-box h3{height:33px;background:var(--navy);color:#fff;font-family:"Montserrat",sans-serif;font-weight:700;font-size:17px;letter-spacing:.5px;text-align:center;padding-top:6px;border-radius:3px 3px 0 0}
.side-box ul{list-style:none;padding:6px 13px;font-size:8.6px;line-height:15.2px;color:#333}
.btn{display:block;margin:6px auto 0;width:98px;height:23px;background:var(--red);color:#fff;font-size:7.5px;text-align:center;line-height:23px;text-decoration:none}
.jobs{display:grid;grid-template-columns:84px 84px;gap:8px;padding:21px 0 0 13px}
.jobs div{height:69px;border:1px solid #fff;background:linear-gradient(135deg,#7e8a96,#c8b9a4)}

/* footer */
.site-footer{left:0;top:967px;width:1159px;height:205px;background:var(--footer);color:#fff}
.site-footer h4{position:absolute;top:14px;font-family:"Arimo",sans-serif;font-weight:400;font-size:15px;color:#ddd}
.sitemap{left:226px;top:45px;list-style:none;font-size:10px;line-height:25px}
.quote{left:446px;top:44px;width:215px;font-size:10px;line-height:15.2px}
.quote-by{left:605px;top:154px;color:var(--link-blue);font-weight:700;font-size:12.5px}
.form{left:730px;top:47px;width:188px}
.form div{border:1px solid #bbb;height:17px;margin-bottom:5px;font-size:8px;color:#aaa;padding:2px 7px}
.form .msg{height:45px}
.form .send{width:80px;margin:3px 0 0 60px;background:#8fa9bd;color:#111;text-align:center;border-color:#ccc}
.copy{left:0;top:1172px;width:1159px;height:28px;background:var(--footer-bar);color:#999;font-size:7.5px;text-align:center;line-height:28px}
</style>
</head>
<body>
<header class="abs site-header">
  <div class="abs brand"><span class="brand-mark"></span><span class="brand-name">Sierra Crest Plumbing</span></div>
  <div class="abs call">Call now<span class="num">909-555-0147</span></div>
</header>
<nav class="abs main-nav">
  <a href="#" style="left:234px">HOME</a>
  <a href="#" style="left:294px">SERVICES</a>
  <a href="#" style="left:369px">RECENT JOBS</a>
  <a href="#" style="left:462px">CONTACT US</a>
</nav>

<div class="abs hero-band"></div>
<section class="abs hero">
  <div class="hero-photo" role="img" aria-label="Plumber repairing a bathroom sink beside brass pipe fittings"></div>
  <div class="abs hero-text">WHY USE SIERRA CREST PLUMBING<br>WE ARE LOCAL FASTER SERVICE<br>NO COMMISSIONED SALES PEOPLE<br>FULLY EQUIPPED TRUCKS PARTS AND TOOLS</div>
  <svg class="abs hero-arrow" style="left:8px" width="20" height="40" viewBox="0 0 20 40"><path d="M16 2 L4 20 L16 38" fill="none" stroke="#fff" stroke-width="3"/></svg>
  <svg class="abs hero-arrow" style="left:712px" width="20" height="40" viewBox="0 0 20 40"><path d="M4 2 L16 20 L4 38" fill="none" stroke="#fff" stroke-width="3"/></svg>
  <div class="abs hero-dots"><span>1</span><span>2</span><span>3</span><span>4</span></div>
</section>

<div class="abs drops left" role="img" aria-label="Water droplets background"></div>
<div class="abs drops right" role="img" aria-label="Water droplets background"></div>
<main class="abs content"></main>

<section class="abs welcome">
  <h1>Welcome to Sierra Crest Plumbing</h1>
  <p><b>Sierra Crest Plumbing</b> is the industry leader in the area. We are a Plumbing, Drain Cleaning, and General Engineering contractors, providing excellent customer service and helping homeowners to live more comfortable and healthy lives.</p>
  <p>If you are looking for a Plumber in Cedar Hollow then call on <b>Sierra Crest Plumbing</b> as your Plumbing Contractor.</p>
  <p>When the water heater bursts or the bathroom is flooding, do you want the best plumber available, or do you want the cheapest? At Sierra Crest Plumbing, we know that the best plumber does world-class work, is fully licensed and insured, is available 24/7 – including during emergencies – and somehow combines world-class equipment and service with world-class affordability.</p>
</section>

<article class="abs service" style="top:575px">
  <h2>PLUMBING</h2>
  <div class="body"><div class="thumb" role="img" aria-label="Wrench on a pipe fitting"></div>We are a full-service plumbing company. Our plumbers are experts at repairing or replacing all types of leaks, faucets, toilets, water heaters, drain and sewer pipes, water lines, gas lines/earthquake valves, garbage disposers, and re-circulating pumps.<div style="clear:both"></div></div>
</article>
<article class="abs service" style="top:694px">
  <h2>DRAIN CLEANING</h2>
  <div class="body"><div class="thumb" role="img" aria-label="Wrench on a pipe fitting"></div>We have been cleaning drains for almost 20 years. Whether it's a kitchen sink or a main sewer line stoppage, we have cleaned them all! We are equipped with some of the newest technology available from color sewer camera's with electronic line locator's and trench-less sewer repairs, we stay up to date to save you money!<div style="clear:both"></div></div>
</article>
<article class="abs service" style="top:812px">
  <h2>GENERAL ENGINEERING</h2>
  <div class="body"><div class="thumb" role="img" aria-label="Wrench on a pipe fitting"></div>What sets us apart, is being a class "A" engineering contractor. On larger projects that require cutting concrete and asphalt, excavating, repairing larger pipe, or entering into the city right of way- We CAN handle it. Other contractors must sub-contract work like this, we do it all in-house. On commercial properties, we learn every aspect of the domestic water, fire water, irrigation supply, sewer and storm drain system, when something fails, we already know where everything is and how to solve the problem quickly. In addition to normal plumbing products, we keep 4, 6 and 8" water fittings. After hour emergencies are handled with ease.</div>
</article>

<aside class="abs side-box" style="top:394px;height:307px">
  <h3>OUR SERVICES</h3>
  <ul>
    <li>Backflow Preventers / Backflow Testing</li><li>Catch Basins</li><li>Ceiling Leaks / Leaks thru the ceiling</li><li>Circulator Pumps / Water Heater Pumps</li><li>Clogged Drains / Sewer Back Ups</li><li>Commercial</li><li>Copper Piping / PEX re-piping</li><li>Drain Cleaning</li><li>Electric Water Heaters</li><li>Encroachment Permits</li><li>Excavation</li><li>Faucets Leaking / Dripping Fixtures</li><li>Fire Hydrants</li><li>Fire Line</li><li>Garbage Disposals</li>
  </ul>
  <a class="btn" href="#" style="margin-top:0">Learn more &#10140;</a>
</aside>
<aside class="abs side-box" style="top:711px;height:246px">
  <h3>RECENT JOBS</h3>
  <div class="jobs">
    <div role="img" aria-label="Sewer jetting truck on a job site"></div>
    <div role="img" aria-label="Plumber fitting pipes under a sink"></div>
    <div role="img" aria-label="Crew excavating a sewer line"></div>
    <div role="img" aria-label="Plumber repairing a fixture"></div>
  </div>
  <a class="btn" href="#" style="margin-top:15px">Learn more &#10140;</a>
</aside>

<footer class="abs site-footer">
  <h4 style="left:225px">Sitemap</h4>
  <ul class="abs sitemap"><li>Home</li><li>Services</li><li>Recent Jobs</li><li>Contact Us</li></ul>
  <h4 style="left:443px">What people say about us</h4>
  <p class="abs quote">Lorem Ipsum. Proin gravida nibh vel velit auctor aliquet. Aenean sollicitudin, lorem quis bibendum auctor, nisi elit consequat ipsum, nec sagittis sem nibh id elit. Duis sed odio sit amet nibh vulputate cursus a sit amet mauris. Morbi accumsan ipsum velit. Nam nec tellus a odio tincidunt</p>
  <div class="abs quote-by">- Dana R.</div>
  <h4 style="left:730px">Quick contact</h4>
  <div class="abs form">
    <div>Name</div><div>Phone no.</div><div>Email</div><div class="msg">Message</div><div class="send">Send</div>
  </div>
</footer>
<div class="abs copy">Copyright © 2013 Sierra Crest Plumbing. All right reserved.</div>
</body>
</html>
```